Flyer for corporate discount for dog daycare

I own a dog daycare with a large corporate down the road. I am working with the President of the company to offer their employees a discount for my services, Dog Daycare, Overnight Care, Grooming Salon & Spa and Retail. The design should be professional but also have a soft side as people view their dogs similar to human children.

I attached my logo along with our grooming brochure for reference on colors we've been using.

At a minimum the flyer must contain the following information:
Name: The Wagtail Lodge
web address: www.PawHavenStays.example
phone number: 920-555-0148
Address: 4872 Larchmont Lane
Google Map of our location

Title of flyer/program: Corporate V.I.P. (Very Important Pooch) (Can be creative with how to include this such as, Welcome to our Corporate. . .. etc.)

The program offer is: 5% discount
My services: Dog Daycare, Overnight Care, Grooming Salon & Spa and Retail

Target Market(s)

corporate employees, male and female, age 24+

Industry/Entity Type

Daycare

Requirements
Must have
• Must be easy to read and inviting.
Nice to have
• Nice photo dogs playing or inviting photo of dog.
Should not have
• cartoon feel

```html
<!DOCTYPE html>
<html lang="en">
<head>
<meta charset="utf-8">
<title>The Wagtail Lodge – Corporate V.I.P. Flyer</title>
<link href="https://fonts.googleapis.com/css2?family=Arimo:wght@400;700&display=swap" rel="stylesheet">
<style>
:root{
  --backdrop:#e9ecee;
  --paper:#ffffff;
  --paper-tint:#f1f8fa;
  --brand-brown:#5a4636;
  --brand-blue:#1f5fa0;
  --sky:#a9dde3;
  --leaf:#8cc63f;
  --ink:#222222;
  --body:#3a3a3a;
  --muted:#7a7a7a;
  --map-land:#e4eadf;
  --map-road:#ffffff;
}
*{box-sizing:border-box;margin:0;padding:0}
html,body{width:857px;height:1200px;overflow:hidden}
body{background:var(--backdrop);font-family:"Arimo",Arial,sans-serif;position:relative}
.flyer{position:absolute;left:68px;top:90px;width:720px;height:1018px;background:linear-gradient(180deg,var(--paper) 0%,var(--paper-tint) 100%);overflow:hidden;box-shadow:0 6px 18px rgba(0,0,0,.18)}

.brand{position:absolute;left:64px;top:22px;width:190px;z-index:2}
.brand-mark{display:block;width:64px;height:64px;background:var(--brand-brown);margin-left:51px}
.brand-name{display:block;margin-top:8px;font-size:17px;font-weight:400;color:var(--brand-brown);letter-spacing:.4px;white-space:nowrap}
.brand-tagline{display:block;margin-top:3px;font-size:8px;color:var(--ink);white-space:nowrap;word-spacing:2px}

.headline{position:absolute;left:274px;top:24px;font-size:33px;font-weight:400;color:var(--ink);letter-spacing:-1px;white-space:nowrap}
.subhead{position:absolute;left:276px;top:64px;font-size:21px;letter-spacing:3px;color:var(--ink);white-space:nowrap}

.hero{position:absolute;left:0;top:95px;width:720px;height:385px;z-index:1}

.offer-badge{position:absolute;left:107px;top:180px;width:160px;height:160px;border-radius:50%;background:var(--sky);border:5px solid #fff;display:flex;flex-direction:column;align-items:center;justify-content:center;transform:rotate(-14deg);color:var(--ink);font-weight:700;text-align:center;line-height:1.1;z-index:3}
.offer-badge .t1{font-size:19px}
.offer-badge .t2{font-size:19px}
.offer-badge .t3{font-size:11.5px}

.offer-note{position:absolute;left:50px;top:340px;width:322px;font-size:12.8px;font-weight:700;line-height:1.4;color:#fff;z-index:3}

.hours{position:absolute;left:560px;top:448px;width:104px;height:104px;border-radius:50%;background:var(--leaf);display:flex;flex-direction:column;align-items:center;justify-content:center;font-size:10.5px;line-height:1.3;color:var(--ink);text-align:center;z-index:3}

.services-title{position:absolute;left:65px;top:497px;font-size:30px;font-weight:400;color:var(--brand-blue);letter-spacing:-.3px}

.service-col{position:absolute;top:539px;list-style:none}
.service-col.left{left:40px;width:322px}
.service-col.right{left:384px;width:302px}
.service{position:relative;padding-left:25px;margin-bottom:17px}
.service-col.left .service{margin-bottom:14px}
.service-arrow{position:absolute;left:0;top:0;width:17px;height:17px}
.service-name{font-size:14.5px;font-weight:700;color:var(--brand-blue);line-height:1.2}
.service-text{font-size:12.8px;color:var(--body);line-height:1.3}

.fine-print{position:absolute;left:50px;top:882px;width:470px;height:46px;border:1.5px solid var(--leaf);border-radius:8px;padding:3px 10px;font-size:9px;line-height:1.3;color:var(--muted);text-align:center}
.location-map{position:absolute;left:530px;top:882px;width:140px;height:46px;border:1.5px solid var(--leaf);border-radius:8px;overflow:hidden}

.cta-band{position:absolute;left:0;top:932px;width:720px;height:60px;background:var(--leaf);display:flex;align-items:center;justify-content:center;gap:20px;color:var(--ink)}
.cta-paw{position:absolute;top:14px;width:32px;height:32px}
.cta-text{font-size:22px}
.cta-phone{display:flex;align-items:center;gap:8px;font-size:30px}

.contact-bar{position:absolute;left:40px;top:1000px;width:640px;display:flex;justify-content:space-between;font-size:10.5px;color:var(--ink)}
.contact-item{display:flex;align-items:center;gap:5px;white-space:nowrap}
</style>
</head>
<body>
<main class="flyer">
  <header class="brand">
    <span class="brand-mark"></span>
    <span class="brand-name">THE WAGTAIL LODGE</span>
    <span class="brand-tagline">DAYCARE OVERNIGHT CARE GROOMING RETAIL</span>
  </header>
  <h1 class="headline">WELCOME TO OUR V.I.P’S</h1>
  <p class="subhead">(Very important Pooch)</p>

  <svg class="hero" viewBox="0 0 720 385" xmlns="http://www.w3.org/2000/svg">
    <defs>
      <linearGradient id="lawn" x1="0" y1="0" x2="0" y2="1">
        <stop offset="0" stop-color="#7f9a4a"/>
        <stop offset=".45" stop-color="#5f8a2e"/>
        <stop offset="1" stop-color="#3f6e1f"/>
      </linearGradient>
      <radialGradient id="dogtone" cx=".72" cy=".45" r=".35">
        <stop offset="0" stop-color="#a8561f" stop-opacity=".85"/>
        <stop offset="1" stop-color="#a8561f" stop-opacity="0"/>
      </radialGradient>
    </defs>
    <g role="img" aria-label="Photo of a golden retriever running across a lawn with a tennis ball">
      <rect x="0" y="20" width="720" height="350" fill="url(#lawn)"/>
      <rect x="0" y="20" width="720" height="350" fill="url(#dogtone)"/>
    </g>
    <path d="M0,0 H720 V14 C600,22 470,36 350,44 C230,52 110,50 0,44 Z" fill="#fff"/>
    <path d="M0,44 C110,50 230,52 350,44 C470,36 600,22 720,14 V30 C600,34 480,48 350,54 C220,60 100,58 0,52 Z" fill="var(--sky)"/>
    <path d="M260,44 C420,30 560,12 720,8 V40 C600,26 460,32 260,44 Z" fill="var(--leaf)"/>
    <path d="M0,318 C120,340 260,360 380,352 C500,344 620,330 720,332 V385 H0 Z" fill="#fff"/>
    <path d="M0,318 C120,340 260,360 380,352 C260,368 120,356 0,340 Z" fill="var(--leaf)"/>
    <path d="M330,352 C460,338 600,322 720,318 V336 C600,334 480,346 330,352 Z" fill="var(--sky)"/>
  </svg>

  <div class="offer-badge">
    <span class="t1">SPECIAL OFFER</span>
    <span class="t2">5% Discount</span>
    <span class="t3">for corporate V.I.P.s</span>
  </div>
  <p class="offer-note">As a corporate V.I.P., employees of our partner company enjoy 5% off Dog Daycare, Overnight Care, Grooming Salon &amp; Spa and Retail. Just show your company ID at check-in.</p>

  <div class="hours"><span>Time on Mon-Fri</span><span>6AM-6PM</span><span>Sat 8AM-6PM</span><span>Sun 10AM-6PM</span></div>

  <h2 class="services-title">SPA SERVICES A LA CARTE</h2>

  <ul class="service-col left">
    <li class="service">
      <svg class="service-arrow" viewBox="0 0 17 17"><circle cx="8.5" cy="8.5" r="8.5" fill="var(--sky)"/><path d="M7 5 L10.5 8.5 L7 12" fill="none" stroke="#1f3b5a" stroke-width="1.4"/></svg>
      <h3 class="service-name">Dental Care: $4</h3>
      <p class="service-text">Teeth are brushed with enzymatic toothpaste that Starts to break down existing tartar while preventing new build up. Finish with a breath spray that works by neutralizing mouth odors and helps to control plaque build up, leaving your pet’s mouth fresh and clean.</p>
    </li>
    <li class="service">
      <svg class="service-arrow" viewBox="0 0 17 17"><circle cx="8.5" cy="8.5" r="8.5" fill="var(--sky)"/><path d="M7 5 L10.5 8.5 L7 12" fill="none" stroke="#1f3b5a" stroke-width="1.4"/></svg>
      <h3 class="service-name">Cleansing facial &amp; Massage: $4</h3>
      <p class="service-text">A lavish massage using our gentle botanical formula of oatmeal and blueberry to help remove tear stains and cleanse without irritating eyes or sensitive skin. Not a stand-alone service, must accompany a Base Service.</p>
    </li>
    <li class="service">
      <svg class="service-arrow" viewBox="0 0 17 17"><circle cx="8.5" cy="8.5" r="8.5" fill="var(--sky)"/><path d="M7 5 L10.5 8.5 L7 12" fill="none" stroke="#1f3b5a" stroke-width="1.4"/></svg>
      <h3 class="service-name">Mango Menngue Massage:$4</h3>
      <p class="service-text">Organic mango butter long with coconut, blueberries, wild fruit, and vitamin E deeply moisturize and soothe dry, damaged paws, elbows, and noses.</p>
    </li>
  </ul>

  <ul class="service-col right">
    <li class="service">
      <svg class="service-arrow" viewBox="0 0 17 17"><circle cx="8.5" cy="8.5" r="8.5" fill="var(--sky)"/><path d="M7 5 L10.5 8.5 L7 12" fill="none" stroke="#1f3b5a" stroke-width="1.4"/></svg>
      <h3 class="service-name">Ear Cleaning:$4</h3>
      <p class="service-text">Regular cleaning will help protect against ear infections.</p>
    </li>
    <li class="service">
      <svg class="service-arrow" viewBox="0 0 17 17"><circle cx="8.5" cy="8.5" r="8.5" fill="var(--sky)"/><path d="M7 5 L10.5 8.5 L7 12" fill="none" stroke="#1f3b5a" stroke-width="1.4"/></svg>
      <h3 class="service-name">Flea &amp; Tick Preventative:$10</h3>
      <p class="service-text">Monthly topical application to gelp protect your pup from fleas, ticks, and mosquitos.</p>
    </li>
    <li class="service">
      <svg class="service-arrow" viewBox="0 0 17 17"><circle cx="8.5" cy="8.5" r="8.5" fill="var(--sky)"/><path d="M7 5 L10.5 8.5 L7 12" fill="none" stroke="#1f3b5a" stroke-width="1.4"/></svg>
      <h3 class="service-name">Facial Trim or Hygiene Trim:$10</h3>
      <p class="service-text">Keep our pet looking and feeling their best between grooms with a trim.</p>
    </li>
    <li class="service">
      <svg class="service-arrow" viewBox="0 0 17 17"><circle cx="8.5" cy="8.5" r="8.5" fill="var(--sky)"/><path d="M7 5 L10.5 8.5 L7 12" fill="none" stroke="#1f3b5a" stroke-width="1.4"/></svg>
      <h3 class="service-name">Brush out:$10</h3>
      <p class="service-text">A between grooming brush out will help remove dead hair and bander. Rate based on 20 minutes of brushing.</p>
    </li>
    <li class="service">
      <svg class="service-arrow" viewBox="0 0 17 17"><circle cx="8.5" cy="8.5" r="8.5" fill="var(--sky)"/><path d="M7 5 L10.5 8.5 L7 12" fill="none" stroke="#1f3b5a" stroke-width="1.4"/></svg>
      <h3 class="service-name">Nail Trim:$10-$14</h3>
      <p class="service-text">If you hear your pet’s nails clicking on the floor, it’s time for a trim!</p>
    </li>
  </ul>

  <p class="fine-print">Documented proof of required vaccines is necessary prior to services. Additional charges may be applied due to the condition of the coat or behaviour resulting in increased grooming time. If any pet is found to have fleas at time of service, extra bathing and service fees will apply starting at $30.</p>

  <svg class="location-map" viewBox="0 0 140 46" role="img" aria-label="Map showing The Wagtail Lodge at 4872 Larchmont Lane, Neenah">
    <rect width="140" height="46" fill="var(--map-land)"/>
    <path d="M0 30 H140" stroke="var(--map-road)" stroke-width="5"/>
    <path d="M48 0 V46" stroke="var(--map-road)" stroke-width="4"/>
    <path d="M96 0 L118 46" stroke="var(--map-road)" stroke-width="3"/>
    <path d="M76 8a6 6 0 0 1 6 6c0 5-6 12-6 12s-6-7-6-12a6 6 0 0 1 6-6z" fill="var(--brand-blue)"/>
    <circle cx="76" cy="14" r="2.2" fill="#fff"/>
  </svg>

  <section class="cta-band">
    <svg class="cta-paw" style="left:16px" viewBox="0 0 32 32"><g fill="#e9f4d6"><ellipse cx="16" cy="21" rx="7" ry="6"/><circle cx="7" cy="13" r="3.2"/><circle cx="12.5" cy="7.5" r="3.2"/><circle cx="19.5" cy="7.5" r="3.2"/><circle cx="25" cy="13" r="3.2"/></g></svg>
    <span class="cta-text">Schedule an appointment today</span>
    <span class="cta-phone">
      <svg width="26" height="26" viewBox="0 0 26 26"><rect x="2" y="7" width="22" height="17" rx="2" fill="#222"/><rect x="4" y="2" width="18" height="6" rx="3" fill="#222"/><g fill="var(--leaf)"><rect x="6" y="11" width="3" height="3"/><rect x="11.5" y="11" width="3" height="3"/><rect x="17" y="11" width="3" height="3"/><rect x="6" y="17" width="3" height="3"/><rect x="11.5" y="17" width="3" height="3"/><rect x="17" y="17" width="3" height="3"/></g></svg>
      920-555-0148
    </span>
    <svg class="cta-paw" style="right:16px" viewBox="0 0 32 32"><g fill="#e9f4d6"><ellipse cx="16" cy="21" rx="7" ry="6"/><circle cx="7" cy="13" r="3.2"/><circle cx="12.5" cy="7.5" r="3.2"/><circle cx="19.5" cy="7.5" r="3.2"/><circle cx="25" cy="13" r="3.2"/></g></svg>
  </section>

  <footer class="contact-bar">
    <span class="contact-item"><svg width="12" height="12" viewBox="0 0 12 12"><circle cx="6" cy="6" r="6" fill="var(--sky)"/><path d="M6 2.5a2.2 2.2 0 0 1 2.2 2.2C8.2 6.5 6 9.5 6 9.5S3.8 6.5 3.8 4.7A2.2 2.2 0 0 1 6 2.5z" fill="#222"/></svg>4872 Larchmont Lane, Neenah, WI 54956</span>
    <span class="contact-item"><svg width="12" height="12" viewBox="0 0 12 12"><circle cx="6" cy="6" r="5.4" fill="none" stroke="#222" stroke-width="1.1"/><path d="M0.6 6H11.4M6 0.6C3.8 3 3.8 9 6 11.4M6 0.6C8.2 3 8.2 9 6 11.4" fill="none" stroke="#222" stroke-width=".9"/></svg>www.PawHavenStays.example</span>
    <span class="contact-item"><svg width="14" height="10" viewBox="0 0 14 10"><rect width="14" height="10" fill="#333"/><path d="M0 0 L7 5.5 L14 0" fill="none" stroke="#fff" stroke-width="1"/></svg>info@pawhavenstays.example</span>
    <span class="contact-item"><svg width="12" height="12" viewBox="0 0 12 12"><circle cx="6" cy="6" r="6" fill="var(--sky)"/><rect x="3" y="4" width="6" height="4.5" fill="#222"/></svg>920.555.0193</span>
  </footer>
</main>
</body>
</html>
```